Modern Dental Appointment Reminder/Business Card

We already have a beautiful logo and icon picked from here on PixelHarbor, now we need someone to make them into a beautiful business card for us! This business card will also function as an appointment reminder card for patients. It will be double sided and must include:
Front
-Contact Info as Follows:
(Gavin T Morrow, DDS
Family and Cosmetic Dentistry
2947 S 3260 E Ste 400
Farmington, Utah 84093)
-Our Logo or Icon (your choice, if Icon must write "Bluefern Dental" below it like in the example file)
Back
-"You're Invited!"
-"Your next appointment is on"
-Place to write date & time
-"Please call 24hrs ahead if appointment is to be cancelled
-Our Icon

Logo and Icon to be used are attached below, along with an example of what we need.
Please do NOT use lots of red! We want the red to just be an accent. Please use grey, white, or even a muted teal for the majority of the card.

Industry/Entity Type

Dentistry

Contact Information for Business Card

Gavin T Morrow, DDS
2947 S 3260 E Ste 400
Farmington, Utah 84093

Colors
cfeae6

Requirements
Should not have
• Lots of red!

```html
<!DOCTYPE html>
<html lang="en">
<head>
<meta charset="utf-8">
<title>Bluefern Dental – Business &amp; Appointment Card</title>
<link rel="stylesheet" href="https://fonts.googleapis.com/css2?family=Jost:wght@400;500;600&family=Courgette&display=swap">
<style>
  :root {
    --stage: #d9d9d7;
    --card: #ffffff;
    --taupe: #5b534a;
    --taupe-soft: #6a6258;
    --accent-red: #a3201c;
    --ink: #4a433c;
    --rule: #5b534a;
  }
  * { box-sizing: border-box; margin: 0; padding: 0; }
  html, body {
    width: 1200px; height: 970px; overflow: hidden;
    background: var(--stage);
    font-family: "Jost", sans-serif;
    color: var(--ink);
  }
  .card {
    position: absolute; left: 250px; width: 700px; height: 400px;
    background: var(--card);
    box-shadow: 0 10px 30px rgba(0,0,0,.18);
    overflow: hidden;
  }
  .card--front { top: 60px; }
  .card--back { top: 510px; }

  /* Front */
  .front-swoosh { position: absolute; inset: 0; }
  .brand {
    position: absolute; display: flex; align-items: center; gap: 10px;
    font-family: "Jost", sans-serif; font-weight: 600; color: var(--taupe);
  }
  .brand__dot { width: 22px; height: 22px; border-radius: 50%; background: var(--taupe); }
  .card--front .brand { top: 44px; right: 50px; font-size: 26px; }
  .contact {
    position: absolute; right: 50px; top: 150px; text-align: right;
    font-size: 19px; line-height: 1.35; color: var(--ink);
  }
  .contact__title {
    font-weight: 600; font-size: 19px; color: var(--taupe);
    display: inline-block; padding-bottom: 4px; margin-bottom: 10px;
    border-bottom: 2px solid var(--accent-red);
  }

  /* Back */
  .card--back .brand { top: 92px; left: 300px; font-size: 22px; }
  .invite { position: absolute; left: 48px; top: 150px; }
  .invite__title { font-family: "Courgette", cursive; font-size: 38px; color: var(--taupe); }
  .invite__sub { font-size: 15px; margin-top: 2px; }
  .back-address {
    position: absolute; right: 48px; top: 34px; text-align: right;
    font-size: 18px; line-height: 1.35;
  }
  .slot {
    position: absolute; left: 60px; width: 560px; display: flex; align-items: flex-end; gap: 14px;
    font-size: 20px;
  }
  .slot__line { flex: 1; border-bottom: 1.5px dashed var(--rule); height: 1px; margin-bottom: 6px; }
  .slot--date { top: 218px; }
  .slot--time { top: 254px; }
  .phones {
    position: absolute; left: 190px; top: 296px; display: flex; gap: 60px;
    font-size: 20px; letter-spacing: .5px;
  }
  .notice-band {
    position: absolute; left: 0; right: 0; bottom: 22px; height: 46px;
    background: var(--taupe); color: #fff;
    display: flex; align-items: center; justify-content: center;
    font-size: 19px; letter-spacing: .3px;
  }
</style>
</head>
<body>

<section class="card card--front" aria-label="Card front">
  <svg class="front-swoosh" viewBox="0 0 700 400" preserveAspectRatio="none" aria-hidden="true">
    <path d="M0 0 H190 C310 70 370 220 380 400 H0 Z" fill="var(--accent-red)"/>
    <path d="M0 0 H170 C290 72 352 222 362 400 H0 Z" fill="var(--taupe)"/>
  </svg>
  <div class="brand"><span class="brand__dot"></span>Bluefern Dental</div>
  <div class="contact">
    <span class="contact__title">Contact Info</span><br>
    Gavin T Morrow, DDS.<br>
    Family and Cosmetic Dentistry.<br>
    2947 S 3260 E Ste 400<br>
    Farmington, Utah 84093
  </div>
</section>

<section class="card card--back" aria-label="Card back">
  <div class="back-address">2947 S 3260 E Ste 400<br>Farmington, Utah 84093</div>
  <div class="brand"><span class="brand__dot"></span>Bluefern Dental</div>
  <div class="invite">
    <p class="invite__title">You're Invited!</p>
  </div>
  <p class="invite__sub" style="position:absolute;left:48px;top:196px;">Your next appointment is on</p>
  <div class="slot slot--date" style="top:232px;"><span>Date</span><span class="slot__line"></span></div>
  <div class="slot slot--time" style="top:268px;"><span>Time</span><span class="slot__line"></span></div>
  <div class="phones" style="top:300px;"><span>P : 801.555.0142</span><span>F : 801.555.0187</span></div>
  <div class="notice-band">Please call 24hrs ahead if appointment is to be cancelled</div>
</section>

</body>
</html>
```